Flyer DesignFESTIVE, FLORISTRY WORKSHOP

WE NEED A FLYER, TO SEND OUT TO PROSPECTIVE CUSTOMERS, TO ATTEND A ONE DAY CHRISTMAS WORKSHOP, ALL MATERIALS WILL BE SUPPLIED AND SO TO WE WILL PROVIDE REFRESHMENTS, PARTICIPIANTS JUST NEED TO BRING THIER FLORISTRY SCISSORS

ON THE DAY THE WILL PARTICIPIATE IN CREATING SEASONAL FLORISTRY DESIGNS THAT THEY CAN BRING HOME TO LAST THE FESTIVE SEASON,

MAREIKE AND LORNA WILL BE THERE WITH SOME UNIQUE IDEAS TO ENHANCE OUR CHRISTMAS FESTIVITIES. TOTAL COST FOR THE DAY IS £79.00. AND THE DATE IS 6THDECEMBER, 2014, AT THE BRAMBLEGATE HOTEL DUNMARREN, WHICH HAS ALSO A BUS LINK TO MANY OTHER AREAS, SO ENJOY YOURSELVES, GET INTO THE FESTIVE FEELING ON THIS SPECIAL OCCASION

FLOWER LOVERS THAT LIKE TO CREATE THIER OWN FLORAL DESIGNS

Hotel

Decorative

Must have
• A CHRISTMAS ATMOSPHERE, WITH A BEAUTIFUL DOOR WREATH AND TABLE DESIGN

BOTH TUTORS ON THE DAY ARE HIGHLY SKILLED, HIGHLY QUALIFIED, WITH LORNA, HAVING WON GFA WEXLEY MEDAL,
Nice to have
• BETTER WORDING THAN I HAVE GIVEN YOU

telephone number 02894412385

```html
<!DOCTYPE html>
<html lang="en">
<head>
<meta charset="utf-8">
<title>Create Your Own Floral Design – Festive Floristry Workshop</title>
<link href="https://fonts.googleapis.com/css2?family=Anton&family=Rye&family=Josefin+Sans:wght@400;600&family=Pathway+Gothic+One&family=Amatic+SC:wght@400;700&display=swap" rel="stylesheet">
<style>
  :root {
    --ink: #1c1c18;
    --forest: #2f3a20;
    --moss: #3d4a2a;
    --parchment: #d9cb8d;
    --banner-text: #3d3b30;
    --wood-light: #f1efe9;
    --wood-mid: #dcd8cf;
    --wreath-green: #8f9a78;
    --wreath-orange: #c9714a;
  }
  html, body {
    margin: 0;
    padding: 0;
    overflow: hidden;
    background: var(--wood-light);
  }
  .flyer {
    position: relative;
    width: 850px;
    height: 1200px;
    overflow: hidden;
    background: var(--wood-light);
    color: var(--ink);
  }
  .flyer-art {
    position: absolute;
    inset: 0;
  }
  .text {
    position: absolute;
    margin: 0;
    white-space: nowrap;
  }
  .title-main {
    top: 44px; left: 200px; width: 530px;
    text-align: center;
    font-family: "Anton", sans-serif;
    font-weight: 400;
    font-size: 76px;
    line-height: 1;
    color: var(--forest);
    letter-spacing: 0;
  }
  .title-script {
    top: 120px; left: 115px; width: 580px;
    text-align: center;
    font-family: "Rye", serif;
    font-weight: 400;
    font-size: 58px;
    line-height: 1;
    color: var(--moss);
    letter-spacing: 3px;
  }
  .scissors-note {
    top: 368px; left: 100px; width: 640px;
    text-align: center;
    font-family: "Josefin Sans", sans-serif;
    font-weight: 600;
    font-variant: small-caps;
    font-size: 27px;
    color: var(--banner-text);
  }
  .tutor-help {
    top: 404px; left: 100px; width: 640px;
    text-align: center;
    font-family: "Josefin Sans", sans-serif;
    font-size: 18px;
    letter-spacing: 1px;
    color: var(--banner-text);
  }
  .festive-message {
    top: 512px; left: 118px; width: 610px;
    text-align: center;
    font-family: "Pathway Gothic One", sans-serif;
    font-size: 56px;
    line-height: 58px;
    color: var(--banner-text);
  }
  .tutor-credentials {
    top: 740px; left: 120px; width: 615px;
    text-align: center;
    font-family: "Josefin Sans", sans-serif;
    font-variant: small-caps;
    font-size: 21px;
    color: var(--banner-text);
  }
  .tutor-medal {
    top: 775px; left: 120px; width: 615px;
    text-align: center;
    font-family: "Josefin Sans", sans-serif;
    font-weight: 600;
    font-variant: small-caps;
    font-size: 24px;
    color: var(--banner-text);
  }
  .details {
    font-family: "Amatic SC", cursive;
    font-weight: 400;
    color: var(--ink);
  }
  .cost {
    top: 905px; right: 40px;
    font-size: 64px;
    line-height: 1;
  }
  .date {
    top: 970px; left: 533px;
    font-size: 54px;
    line-height: 1;
  }
  .phone {
    top: 1026px; left: 243px;
    font-size: 40px;
    line-height: 1;
  }
  .venue {
    top: 1082px; left: 158px;
    font-size: 28px;
    line-height: 1;
  }
  .bus {
    top: 1134px; left: 158px;
    font-size: 23px;
    line-height: 1;
  }
</style>
</head>
<body>
<main class="flyer">
  <svg class="flyer-art" width="850" height="1200" viewBox="0 0 850 1200" xmlns="http://www.w3.org/2000/svg">
    <defs>
      <radialGradient id="wreath-tones" cx="0.42" cy="0.42" r="0.6">
        <stop offset="0" stop-color="#e6e2d8"/>
        <stop offset="0.35" stop-color="#b9b49a"/>
        <stop offset="0.6" stop-color="#a69478"/>
        <stop offset="0.8" stop-color="#c9c3b3"/>
        <stop offset="1" stop-color="#eeece6"/>
      </radialGradient>
      <linearGradient id="table-tones" x1="0" y1="0" x2="1" y2="1">
        <stop offset="0" stop-color="#d8d2c2"/>
        <stop offset="0.5" stop-color="#c9a85a"/>
        <stop offset="1" stop-color="#e9e9e6"/>
      </linearGradient>
    </defs>

    <rect class="wreath-photo" role="img" aria-label="Photo of a dried flower Christmas door wreath with chillies and bay leaves on whitewashed wooden boards" x="0" y="0" width="850" height="1200" fill="url(#wreath-tones)"/>
    <rect class="wood-floor" x="0" y="880" width="850" height="320" fill="var(--wood-light)" opacity="0.75"/>
    <rect class="table-photo" role="img" aria-label="Photo of a workshop table laid with a willow wreath base, flowers and floristry materials" x="400" y="1040" width="450" height="160" fill="url(#table-tones)"/>

    <g class="banner-rigging" stroke="var(--ink)" fill="none">
      <line x1="425" y1="170" x2="425" y2="285" stroke-width="2"/>
      <path d="M425 290 L180 345 M425 290 L665 345" stroke-width="2"/>
      <line x1="228" y1="445" x2="228" y2="718" stroke-width="6"/>
      <line x1="622" y1="445" x2="622" y2="718" stroke-width="6"/>
    </g>

    <g class="banners" fill="var(--parchment)" stroke="var(--ink)" stroke-width="3" stroke-linejoin="round">
      <path class="banner banner-scissors" d="M110,342 Q420,332 730,342 C748,372 722,418 742,448 Q420,440 104,448 C122,418 92,376 110,342Z"/>
      <path class="banner banner-festive" d="M130,462 Q425,454 718,462 C740,520 712,640 728,708 Q425,700 122,710 C140,640 108,540 130,462Z"/>
      <path class="banner banner-tutors" d="M128,716 Q425,706 728,716 C742,748 718,790 736,820 Q425,812 122,822 C140,790 110,750 128,716Z"/>
    </g>

    <g class="icon-clock" fill="none" stroke="var(--ink)" stroke-width="2.5">
      <circle cx="492" cy="998" r="13"/>
      <path d="M492 989 V998 H499"/>
    </g>

    <g class="icon-phone">
      <rect x="190" y="1030" width="30" height="30" rx="5" fill="var(--ink)"/>
      <path d="M198 1037 q-3 4 3 12 q6 7 11 5 l1-3 -4-3 -2 2 q-4-2 -6-7 l2-2 -3-4z" fill="var(--wood-light)"/>
    </g>

    <g class="icon-stop" fill="none" stroke="var(--ink)" stroke-width="2">
      <polygon points="128,1064 142,1064 150,1072 150,1084 142,1092 128,1092 120,1084 120,1072"/>
      <line x1="135" y1="1092" x2="135" y2="1112"/>
      <line x1="128" y1="1113" x2="142" y2="1113"/>
    </g>

    <g class="icon-bus" fill="none" stroke="var(--ink)" stroke-width="2">
      <rect x="75" y="1130" width="65" height="26" rx="4"/>
      <line x1="75" y1="1143" x2="140" y2="1143"/>
      <line x1="90" y1="1130" x2="90" y2="1143"/>
      <line x1="105" y1="1130" x2="105" y2="1143"/>
      <line x1="120" y1="1130" x2="120" y2="1143"/>
      <circle cx="90" cy="1158" r="5" fill="var(--wood-light)"/>
      <circle cx="125" cy="1158" r="5" fill="var(--wood-light)"/>
    </g>
  </svg>

  <h1 class="text title-main">CREATE YOUR OWN</h1>
  <h2 class="text title-script">FLORAL DESIGN</h2>

  <p class="text scissors-note">Just bring your own floristry scissors !</p>
  <p class="text tutor-help">MAREIKE WILL HELP WITH SOME UNIQUE IDEAS</p>

  <p class="text festive-message">SO ENJOY YOURSELVES !<br>GET INTO THE FESTIVE FEELING<br>ON THIS SPECIAL OCCASION</p>

  <p class="text tutor-credentials">Our tutors are HIGHLY SKILLED, HIGHLY QUALIFIED</p>
  <p class="text tutor-medal">with GFA WEXLEY MEDAL</p>

  <p class="text details cost">COST: £79.00</p>
  <p class="text details date">6TH DECEMBER 2014</p>
  <p class="text details phone">02894412385</p>
  <p class="text details venue">BRAMBLEGATE HOTEL DUNMARREN</p>
  <p class="text details bus">BUS LINK TO MANY OTHER AREAS</p>
</main>
</body>
</html>
```